Rowdy ned USA is the name of my childrens book for middle school kids. I'm looking to get a book cover

I'm looking to get an interesting book cover for the book I'm working on called Rowdy USA. It is a book about a middle school kid and his family and friends.It is first one. in a series of books.The book size is 8 1/2 x 5 1/2 .The book is written like a diary much like Tales of a fidgety owl or Pickle Scrolls. It should have the look and feel of a diary or journal. For this first book I wanted to use yellow or gold color for the cover. But if you have a better Idea go for it! I already have a logo which I'll upload for your review which has to go on the cover. I'm looking for unusual and different ideas so please be as creative as you want to be. Thanks

Target Market(s)

Middle school kids ages 9 to 12

Industry/Entity Type

School

Font styles to use
Serif

Colors
ffcf3e
ffc214
ec1f27
f04a51
0456a4
3176b5
85acd3
9ccb3b
acd136

Requirements
Must have
• My Logo ( which is the title of the book. Rowdy Ned USA) I Uploaded it. The Subtitle: Keeping Secrets and Skipping Rope. Main character on the cover. I uploaded two different versions of main characters. Please use either one. Please redraw if necessary.
Nice to have
• Maybe look like a Diary or journal with lock and key or combination lock or different type of diary. But doesn't have to look like that.
Should not have
• The Flag, Stars and stripes,

```html
<!DOCTYPE html>
<html lang="en">
<head>
<meta charset="utf-8">
<title>Rowdy Ned USA – Book Cover</title>
<link rel="stylesheet" href="https://fonts.googleapis.com/css2?family=Francois+One&display=swap">
<style>
  :root {
    --gold-light: #ffcf3e;
    --gold-deep: #ffc214;
    --red: #ec1f27;
    --red-soft: #f04a51;
    --spine-red: #c9262a;
    --blue: #0456a4;
    --blue-mid: #3176b5;
    --navy: #1f2f86;
    --green: #9ccb3b;
    --white: #ffffff;
    --stage: #e6e6e4;
  }
  * { margin: 0; padding: 0; box-sizing: border-box; }
  html, body {
    width: 1200px;
    height: 1000px;
    overflow: hidden;
    background: var(--stage);
    font-family: "Francois One", "Arial Narrow", sans-serif;
  }
  .book {
    position: absolute;
    left: 322px;
    top: 70px;
    width: 556px;
    height: 860px;
    box-shadow: 4px 6px 14px rgba(0,0,0,0.25);
  }
  .spine {
    position: absolute;
    left: 0; top: 0;
    width: 58px; height: 100%;
    background: repeating-linear-gradient(90deg, var(--spine-red) 0 2px, #b91f23 2px 4px);
  }
  .cover {
    position: absolute;
    left: 58px; top: 0; right: 0; bottom: 0;
    background: radial-gradient(ellipse at 50% 40%, var(--gold-light) 0%, var(--gold-deep) 100%);
  }
  .cover-frame {
    position: absolute;
    inset: 14px;
    border: 2px solid var(--red);
  }
  .cover-stitch {
    position: absolute;
    inset: 22px;
    border: 1.5px dashed var(--red);
  }
  .corner {
    position: absolute;
    right: 0;
    width: 54px;
    height: 54px;
  }
  .corner--top { top: 0; }
  .corner--bottom { bottom: 0; transform: scaleY(-1); }

  .title {
    position: absolute;
    top: 92px;
    left: 0; right: 0;
    text-align: center;
    color: var(--red);
    line-height: 0.95;
  }
  .title-main { display: block; font-size: 80px; }
  .title-sub { display: block; font-size: 52px; margin-left: 150px; }

  .subtitle-band {
    position: absolute;
    color: var(--white);
    font-size: 27px;
    letter-spacing: 0.5px;
    padding: 4px 16px 6px;
    text-transform: uppercase;
    white-space: nowrap;
  }
  .subtitle-band--first {
    top: 296px; left: 78px;
    background: var(--blue);
    transform: rotate(-4deg);
  }
  .subtitle-band--joiner {
    top: 300px; left: 348px;
    background: var(--green);
    font-size: 20px;
    padding: 2px 8px 3px;
    transform: rotate(2deg);
  }
  .subtitle-band--second {
    top: 352px; left: 188px;
    background: var(--navy);
    transform: rotate(-2deg);
  }

  .character-art {
    position: absolute;
    left: 120px;
    top: 420px;
    width: 290px;
    height: 380px;
    background: linear-gradient(160deg, #ffffff 0%, #f1f1f1 100%);
    box-shadow: 3px 3px 0 rgba(0,0,0,0.55);
  }
</style>
</head>
<body>
  <div class="book">
    <div class="spine"></div>
    <div class="cover">
      <div class="cover-frame"></div>
      <div class="cover-stitch"></div>

      <svg class="corner corner--top" viewBox="0 0 54 54" aria-hidden="true">
        <path d="M0 0 H54 V54 Q46 14 0 0 Z" fill="#c9262a"/>
      </svg>
      <svg class="corner corner--bottom" viewBox="0 0 54 54" aria-hidden="true">
        <path d="M0 0 H54 V54 Q46 14 0 0 Z" fill="#c9262a"/>
      </svg>

      <h1 class="title">
        <span class="title-main">Rowdy Ned</span>
        <span class="title-sub">USA</span>
      </h1>

      <div class="subtitle-band subtitle-band--first">Keeping Secrets</div>
      <div class="subtitle-band subtitle-band--joiner">and</div>
      <div class="subtitle-band subtitle-band--second">Skipping Rope</div>

      <div class="character-art" role="img" aria-label="Taped-on cut-out sketch of the main character, a smiling boy holding his journal"></div>
    </div>
  </div>
</body>
</html>
```